Home care agency

Current website QRVCAREPLUS.com. Need to update and reformat to different pages. use my info from my current website

Target Market(s)

adult children

Industry/Entity Type

Home Health

Coding

Coded - Design and coding required

Number of Pages Required

4 page

Font styles to use
Sans Serif

Colors
3276b5
33a6d7
3277b5
85cae6
85acd3

```html
<!DOCTYPE html>
<html lang="en">
<head>
<meta charset="utf-8">
<title>Quiet River Care Services</title>
<link rel="stylesheet" href="https://fonts.googleapis.com/css2?family=Montserrat:wght@300;400;500;600;700&display=swap">
<style>
:root{
  --blue:#3276b5;
  --navy:#1f4a8a;
  --heading:#2b5a98;
  --sky:#33a6d7;
  --teal:#5fd0c0;
  --ink:#3d4a5a;
  --body:#6d7886;
  --soft:#f5f6f8;
  --line:#c9ced6;
  --field:#eef0f3;
  --dark:#262c36;
}
*{box-sizing:border-box;margin:0;padding:0}
html,body{width:1200px;height:3442px;overflow:hidden}
body{position:relative;font-family:'Montserrat',sans-serif;color:var(--body);background:#fff}
.abs{position:absolute}
p{font-size:12.5px;line-height:14.6px;font-weight:400}

/* header */
.site-header{left:0;top:0;width:1200px;height:139px;background:#fff}
.brand{left:175px;top:20px;width:105px;height:105px;border:2px solid var(--sky);border-radius:50%;display:flex;align-items:center;justify-content:center;font-size:20px;font-weight:500;color:var(--blue);letter-spacing:1px}
.nav a{position:absolute;top:70px;font-size:12px;font-weight:700;color:#222;text-decoration:none;letter-spacing:.3px}
.header-contact{right:171px;top:58px;text-align:right;font-size:11.5px;line-height:16px;color:#333}

/* hero */
.hero-photo{left:0;top:139px;width:1200px;height:605px;background:linear-gradient(100deg,#8a7a6a 0%,#5e5048 35%,#4a3f3b 60%,#6a5d55 100%)}
.hero-shade{left:0;top:139px;width:1200px;height:605px;background:rgba(30,35,45,.25)}
.hero-title{left:0;top:386px;width:1224px;text-align:center;color:#fff;font-size:46px;line-height:56px;font-weight:400;letter-spacing:1.5px}
.hero-sub{left:0;top:508px;width:1212px;text-align:center;color:#fff;font-size:23px;font-weight:700}
.hero-btn{left:400px;top:576px;width:398px;height:63px;border:2.5px solid #fff;border-radius:20px;color:#fff;font-size:23px;display:flex;align-items:center;justify-content:center;letter-spacing:.8px}
.hero-arrow{left:580px;top:692px}

/* about */
.about-photo{left:175px;top:839px;width:287px;height:273px;background:linear-gradient(160deg,#c8b49a,#8b7f8c 55%,#5b5062)}
.section-title{font-size:37px;font-weight:400;color:var(--ink);letter-spacing:.8px}
.rule{width:70px;height:2px;background:var(--teal)}
.about-text{left:498px;top:920px;width:530px}
.about-text p+p{margin-top:14px}

/* services */
.services-band{left:0;top:1165px;width:1192px;height:501px;background:var(--soft)}
.service-img{top:1292px;height:164px}
.service h3{position:absolute;font-size:17px;font-weight:700;color:var(--heading);letter-spacing:.4px}
.service ul{position:absolute;list-style:none;font-size:11.5px;line-height:14.4px}
.service li:before{content:"· "}
.benefits li{padding-left:10px;text-indent:-10px}

/* why / map */
.block-head{font-size:17px;font-weight:700;color:var(--heading);letter-spacing:.4px}
.why p{font-size:11.5px;line-height:14.4px}
.map{left:692px;top:1737px;width:338px;height:361px;border:1.5px solid #555;background:linear-gradient(135deg,#2f6fb3 0%,#3a78b8 40%,#f3f5f8 55%,#ffffff 100%)}

/* contact */
.contact-band{left:0;top:2164px;width:1200px;height:735px;background:var(--soft)}
.form-label{font-size:9.5px;color:#555;font-family:'Montserrat',sans-serif}
.sub-label{font-size:7px;color:#777}
.field{background:var(--field);border:1px solid var(--line)}
.divider{height:1px;background:#9aa3ad}
.radio{width:8px;height:8px;border:1px solid #999;border-radius:50%;background:#fff}
.submit{left:624px;top:2827px;width:128px;height:23px;background:var(--navy);color:#fff;font-size:9px;font-weight:600;display:flex;align-items:center;justify-content:center}

/* info band */
.info h4{position:absolute;top:2934px;font-size:12.5px;font-weight:700;color:#444}
.info p{position:absolute;top:2978px;font-size:12px;line-height:14.6px}
.info em{font-weight:700;font-style:italic}
.download{left:744px;top:3045px;width:126px;height:33px;background:var(--navy);color:#fff;font-size:12.5px;font-weight:700;display:flex;align-items:center;justify-content:center}

/* footer */
.site-footer{left:0;top:3109px;width:1200px;height:333px;background:linear-gradient(120deg,#2e3440 0%,#242a34 50%,#1c222b 100%)}
.footer-brand{left:174px;top:3204px;width:108px;height:110px;background:#fff;display:flex;align-items:center;justify-content:center}
.footer-brand span{width:74px;height:74px;border:2px solid var(--sky);border-radius:50%;display:flex;align-items:center;justify-content:center;color:var(--blue);font-size:14px;font-weight:500}
.footer-about{left:298px;top:3226px;width:170px;font-size:10px;line-height:17px;color:#9aa1ac}
.footer-head{font-size:13px;font-weight:600;color:#fff;letter-spacing:.3px}
.quick-links{left:554px;top:3240px;list-style:none;font-size:10.5px;line-height:17px;color:#9aa1ac}
.quick-links li:before{content:"› ";color:#fff}
.newsletter-text{left:744px;top:3240px;width:240px;font-size:10px;line-height:17px;color:#9aa1ac}
.email-field{left:744px;top:3292px;width:244px;height:28px;background:#5a606a;color:#fff;font-size:10px;padding:10px 0 0 20px}
.email-ok{left:991px;top:3292px;width:39px;height:28px;background:#6d737c;color:#fff;font-size:10px;font-weight:600;display:flex;align-items:center;justify-content:center}
.copyright{left:174px;top:3404px;font-size:10.5px;color:#9aa1ac}
.social{top:3401px;width:22px;height:22px;border-radius:50%;background:#fff}
</style>
</head>
<body>

<header class="site-header abs">
  <div class="brand abs">QRC</div>
  <nav class="nav">
    <a style="left:327px">HOME</a>
    <a style="left:424px">ABOUT</a>
    <a style="left:526px">SERVICES</a>
    <a style="left:644px">CONTACT</a>
  </nav>
  <div class="header-contact abs">PO Box 412 Seabrook, MA 02190<br>Contact: 555-014-2290</div>
</header>

<section class="hero">
  <div class="hero-photo abs" role="img" aria-label="A smiling nurse in a white coat caring for an elderly man seated in a living room"></div>
  <div class="hero-shade abs"></div>
  <h1 class="hero-title abs">Providing Care Throughout<br>the South Shore</h1>
  <div class="hero-sub abs">Quality &amp; Excellence Guaranteed.</div>
  <div class="hero-btn abs">Book an Appointment</div>
  <svg class="hero-arrow abs" width="30" height="20" viewBox="0 0 30 20"><path d="M3 4 Q15 10 27 4 M3 12 Q15 18 27 12" fill="none" stroke="#fff" stroke-width="2.5"/></svg>
</section>

<section class="about">
  <div class="about-photo abs" role="img" aria-label="Portrait of the owner, a registered nurse, seated in a chair"></div>
  <h2 class="section-title abs" style="left:496px;top:830px">About us</h2>
  <div class="rule abs" style="left:498px;top:877px"></div>
  <div class="about-text abs">
    <p>Quiet River Care Services is owned and operated by Laura Bennett. Laura is a registered nurse and has been in the health care system since 2001. She has specialized in home care, cardiology, trauma and critical care. She invests in future caregivers and has taught for the nursing programs at Bayview University, Harborline Institute, and Eastmere College.</p>
    <p>All Quiet River Care caregivers have extensive background checks and training regarding HIPAA compliance. We individualize the care of our clients in order to provide the best care possible in their home. Quiet River Care also ensures full access and understanding of client care at all times with a caregiver binder in the client's home at all times. This binder includes information on the client's care plan along and the notes from their caregivers. This will allow all caregivers and the client's family to have an understanding of the care being provided.</p>
  </div>
</section>

<section class="services">
  <div class="services-band abs"></div>
  <h2 class="section-title abs" style="left:174px;top:1203px">Our Services</h2>
  <div class="rule abs" style="left:175px;top:1261px"></div>

  <div class="service">
    <div class="service-img abs" style="left:174px;width:246px;background:linear-gradient(120deg,#7fc4ad,#c9d3cc 55%,#e8e2dc)" role="img" aria-label="Caregiver's hand resting on an elderly client's shoulder"></div>
    <h3 style="left:180px;top:1478px">SKILLED CARE</h3>
    <ul style="left:178px;top:1506px">
      <li>Free Initial Nursing Assessment</li><li>Medication Management</li><li>Wound Care</li><li>Injections</li><li>Medical Care Assistance</li><li>Transportation to Medical Appointments</li><li>Care Plan Management</li>
    </ul>
  </div>
  <div class="service">
    <div class="service-img abs" style="left:479px;width:248px;background:linear-gradient(120deg,#5a6068,#9aa0a6 55%,#cfd2d6)" role="img" aria-label="Two hands gently holding each other"></div>
    <h3 style="left:493px;top:1478px">NON-MEDICAL</h3>
    <ul style="left:493px;top:1506px">
      <li>Live-In Care</li><li>Respite Care</li><li>Assisting with Daily Living Activities</li><li>Meal Preparations</li><li>Companionship</li><li>Homemaking</li>
    </ul>
  </div>
  <div class="service">
    <div class="service-img abs" style="left:773px;top:1288px;height:168px;width:256px;background:linear-gradient(120deg,#6fa64a,#8dbb5c 50%,#a8c9d8)" role="img" aria-label="Cupped hands holding soil with a small green seedling"></div>
    <h3 style="left:777px;top:1478px">CLIENT BENEFITS</h3>
    <ul class="benefits" style="left:778px;top:1506px;width:240px">
      <li>Continuity of care with same caregiver for each client on a regular basis.</li>
      <li>Open communication with owner by phone or email.</li>
      <li>Ongoing communications to client's family by phone or email on a weekly basis (if desired.)</li>
      <li>Streamlined payment process.</li>
    </ul>
  </div>
</section>

<section class="why">
  <h3 class="block-head abs" style="left:177px;top:1706px">WHY CHOOSE HOME CARE?</h3>
  <p class="abs" style="left:175px;top:1746px;width:485px">Home care is a cost-effective option that allows clients the ability to receive one-on-one care in the comfort of their own home.</p>
  <p class="abs" style="left:175px;top:1790px;width:485px">Home care also provides peace of mind to a client's family, near or far, without taking away a client's independence or privacy.</p>

  <h3 class="block-head abs" style="left:172px;top:1861px">CARE SCHEDULE/FREQUENCY</h3>
  <p class="abs" style="left:177px;top:1896px;width:480px">· Quiet River Care non-medical visits require a four hour minimum visit.</p>
  <p class="abs" style="left:177px;top:1925px;width:480px">· There are no weekly minimum for medical or non-medical visits.</p>
  <p class="abs" style="left:177px;top:1954px;width:480px;padding-left:8px;text-indent:-8px">· Clients needing 24-hour care can save up 30% off of services by using a live-in care giver. (Live-in caregiver requires personal bedroom and bathroom.)</p>

  <h3 class="block-head abs" style="left:172px;top:2031px">PAYMENT OPTIONS</h3>
  <p class="abs" style="left:175px;top:2065px;width:480px">Quiet River Care currently accepts check for service payments (with plans for online payments late 2018.)</p>

  <h3 class="block-head abs" style="left:692px;top:1706px;color:#6a7380">SERVICE AREA MAP</h3>
  <div class="map abs" role="img" aria-label="Map of South Shore towns with the served area shaded in blue"></div>
</section>

<section class="contact">
  <div class="contact-band abs"></div>
  <h2 class="section-title abs" style="left:173px;top:2201px">Contact Us</h2>
  <div class="rule abs" style="left:175px;top:2257px"></div>
  <p class="abs" style="left:173px;top:2278px;width:830px">Thank you for considering Quiet River Care for your care needs. Information about your medical conditions, care, and financial situation that you provide to us in writing, via email, on the phone (including information left on voice mails) is held in strictest confidence.</p>
  <p class="abs" style="left:173px;top:2335px;width:830px">To contact us online, please fill out the care inquiry form below and you will be contacted within 24-48 hours.</p>
  <h3 class="block-head abs" style="left:174px;top:2376px">CARE INQUIRY FORM</h3>

  <form class="inquiry">
    <div class="form-label abs" style="left:175px;top:2424px">Contact Information</div>
    <div class="divider abs" style="left:175px;top:2438px;width:394px"></div>

    <div class="form-label abs" style="left:175px;top:2456px">Contact Name *</div>
    <div class="field abs" style="left:175px;top:2472px;width:192px;height:24px"></div>
    <div class="field abs" style="left:375px;top:2472px;width:194px;height:24px"></div>
    <div class="sub-label abs" style="left:175px;top:2501px">First Name</div>
    <div class="sub-label abs" style="left:375px;top:2501px">Last Name</div>

    <div class="form-label abs" style="left:175px;top:2524px">Contact Phone Number *</div>
    <div class="field abs" style="left:175px;top:2540px;width:40px;height:24px"></div>
    <div class="field abs" style="left:223px;top:2540px;width:40px;height:24px"></div>
    <div class="field abs" style="left:271px;top:2540px;width:47px;height:24px"></div>
    <div class="sub-label abs" style="left:175px;top:2568px">(###)</div>
    <div class="sub-label abs" style="left:223px;top:2568px">###</div>
    <div class="sub-label abs" style="left:271px;top:2568px">####</div>

    <div class="form-label abs" style="left:175px;top:2594px">Contact Email Address *</div>
    <div class="field abs" style="left:175px;top:2608px;width:394px;height:24px"></div>

    <div class="form-label abs" style="left:175px;top:2648px">Best Way to Reach You *</div>
    <div class="radio abs" style="left:175px;top:2663px"></div>
    <div class="sub-label abs" style="left:187px;top:2664px">By Phone</div>
    <div class="radio abs" style="left:175px;top:2676px"></div>
    <div class="sub-label abs" style="left:187px;top:2677px">By Email</div>

    <div class="form-label abs" style="left:175px;top:2703px">Client Information</div>
    <div class="divider abs" style="left:175px;top:2716px;width:394px"></div>

    <div class="form-label abs" style="left:175px;top:2734px">Client Name *</div>
    <div class="field abs" style="left:175px;top:2749px;width:192px;height:24px"></div>
    <div class="field abs" style="left:375px;top:2749px;width:194px;height:24px"></div>
    <div class="sub-label abs" style="left:175px;top:2779px">First Name</div>
    <div class="sub-label abs" style="left:375px;top:2779px">Last Name</div>

    <div class="form-label abs" style="left:175px;top:2802px">Client Birthdate *</div>
    <div class="field abs" style="left:175px;top:2818px;width:33px;height:24px"></div>
    <div class="field abs" style="left:216px;top:2818px;width:34px;height:24px"></div>
    <div class="field abs" style="left:258px;top:2818px;width:47px;height:24px"></div>
    <div class="sub-label abs" style="left:175px;top:2847px">MM</div>
    <div class="sub-label abs" style="left:216px;top:2847px">DD</div>
    <div class="sub-label abs" style="left:258px;top:2847px">YYYY</div>

    <div class="form-label abs" style="left:624px;top:2424px">Address Where Care Will Be Provided *</div>
    <div class="field abs" style="left:624px;top:2440px;width:396px;height:23px"></div>
    <div class="sub-label abs" style="left:624px;top:2468px">Address 1</div>
    <div class="field abs" style="left:624px;top:2496px;width:396px;height:24px"></div>
    <div class="sub-label abs" style="left:624px;top:2525px">Address 2</div>
    <div class="field abs" style="left:624px;top:2553px;width:282px;height:24px"></div>
    <div class="field abs" style="left:914px;top:2553px;width:106px;height:24px"></div>
    <div class="sub-label abs" style="left:624px;top:2583px">City</div>
    <div class="sub-label abs" style="left:914px;top:2583px">State/Province</div>
    <div class="field abs" style="left:624px;top:2609px;width:146px;height:24px"></div>
    <div class="sub-label abs" style="left:624px;top:2639px">Zip/Postal Code</div>
    <div class="field abs" style="left:624px;top:2667px;width:396px;height:24px"></div>
    <div class="sub-label abs" style="left:624px;top:2696px">Country</div>
    <div class="form-label abs" style="left:624px;top:2720px;width:396px;font-size:8.5px;line-height:11px">Please use this area to tell us more about the client and/or services that may be of interest to you. *</div>
    <div class="field abs" style="left:624px;top:2747px;width:396px;height:59px"></div>
    <div class="submit abs">Submit Care Inquiry</div>
  </form>
</section>

<section class="info">
  <h4 style="left:173px">Contact By Phone</h4>
  <p style="left:173px;width:245px">If you would like to speak with someone over the phone about your care inquiry, you can contact Quiet River Care Monday-Friday 9:00am-5:00pm at 555-014-2290.</p>
  <h4 style="left:458px">Mailing Address</h4>
  <p style="left:459px;width:250px">Please mail all service payments and employment applications to: <em>Quiet River Care Services PO Box 412 Seabrook, MA 02190</em></p>
  <h4 style="left:745px">Employment Application</h4>
  <p style="left:743px;width:270px">To apply with QRCS, Kindly download the following form and submit it to our mailing address or email it at <i>Laura@qrvcareplus.com</i></p>
  <div class="download abs">Download Form</div>
</section>

<footer class="site-footer abs">
</footer>
<div class="abs" role="img" aria-label="Faint background photo of hands held together" style="left:0;top:3109px;width:1200px;height:333px"></div>
<div class="footer-brand abs"><span>QRC</span></div>
<div class="footer-about abs">Lorem ipsum dolor sit amet, consectetur adipiscing elit. Vestibulum gravida quam quis nunc rutrum placerat. Proin eu</div>
<div class="footer-head abs" style="left:550px;top:3210px">QUICK LINKS</div>
<ul class="quick-links abs"><li>Home</li><li>About</li><li>Services</li><li>Contact Us</li></ul>
<div class="footer-head abs" style="left:745px;top:3210px">JOIN OUR NEWSLETTER</div>
<div class="newsletter-text abs">Lorem ipsum dolor sit amet dolor consectetur adipiscing elit.</div>
<div class="email-field abs">Email</div>
<div class="email-ok abs">OK</div>
<div class="copyright abs">© All Rights Reserved by Quiet River Care Services</div>
<div class="social abs" style="left:900px"></div>
<div class="social abs" style="left:952px"></div>
<div class="social abs" style="left:1007px"></div>

</body>
</html>
```